Business Card Design Project

We need a Business Card Design for our Architectural Company, we want the cards to stand out WOW factor, we are thinking to have the logo on the front and embossed and all the contact info etc on the back. however we are open to suggestions
Updates

Reason: would like more submissions, just posted the brief

Target Market(s)

Adults looking for a Architect for their design project, or a developers who need an architecture firm to partner with. Card should be very powerful and portray elegance and creativity as first impression

Industry/Entity Type

Business

Requirements
Must have
• Must have large logo and easy to read address info, current card attached for address and contact info that should be on card.

```html
<!DOCTYPE html>
<html lang="en">
<head>
<meta charset="utf-8">
<title>Coral Ridge Design Studio – Business Card</title>
<link rel="stylesheet" href="https://fonts.googleapis.com/css2?family=Arimo&family=Montserrat:wght@700&family=Tinos&display=swap">
<style>
  :root {
    --orange: #e8540a;
    --navy: #2e2f86;
    --paper: #ffffff;
    --backdrop: #e4e4e4;
    --ink-light: #ffffff;
  }
  * { box-sizing: border-box; margin: 0; padding: 0; }
  html, body { width: 1200px; height: 800px; overflow: hidden; }
  body { background: var(--backdrop); position: relative; }

  .card {
    position: absolute;
    width: 620px;
    height: 360px;
    background: var(--paper);
    overflow: hidden;
    box-shadow: 0 2px 6px rgba(0,0,0,0.15);
  }
  .card-shapes { position: absolute; inset: 0; width: 100%; height: 100%; }
  .card-front { left: 70px; top: 50px; }
  .card-back { left: 520px; top: 400px; }

  .brand {
    position: absolute;
    display: flex;
    align-items: flex-start;
    gap: 12px;
    font-family: "Montserrat", sans-serif;
    font-weight: 700;
    color: var(--navy);
    line-height: 1.05;
    white-space: nowrap;
  }
  .brand-square { width: 18px; height: 18px; background: var(--navy); flex: none; margin-top: 8px; }
  .card-front .brand { left: 60px; top: 128px; }
  .card-front .brand-main { font-size: 46px; letter-spacing: 1px; }
  .card-front .brand-sub { font-size: 25px; letter-spacing: 1px; }

  .card-back .brand {
    left: 18px; top: 340px;
    transform: rotate(-90deg);
    transform-origin: left top;
  }
  .card-back .brand-square { width: 12px; height: 12px; margin-top: 5px; }
  .card-back .brand-main { font-size: 30px; }
  .card-back .brand-sub { font-size: 16px; }

  .holder {
    position: absolute; left: 250px; top: 100px; width: 300px;
    text-align: center; color: var(--ink-light);
    font-family: "Arimo", sans-serif;
  }
  .holder-name { font-size: 25px; }
  .holder-title { font-size: 15px; margin-top: 6px; }

  .address {
    position: absolute; left: 230px; top: 212px;
    font-family: "Tinos", serif; font-size: 17px; line-height: 23px;
    color: var(--ink-light); font-style: normal;
    white-space: nowrap;
  }
  .contacts {
    position: absolute; left: 460px; top: 188px;
    list-style: none;
    font-family: "Tinos", serif; font-size: 13px; line-height: 25px;
    color: var(--ink-light);
    white-space: nowrap;
  }
  .contacts li { display: flex; align-items: center; gap: 7px; }
  .contacts svg { width: 13px; height: 13px; flex: none; }
</style>
</head>
<body>

<section class="card card-front" aria-label="Card front">
  <svg class="card-shapes" viewBox="0 0 620 360" aria-hidden="true">
    <polygon fill="var(--orange)" points="0,0 150,0 0,72"/>
    <polygon fill="var(--orange)" points="0,245 0,360 135,360"/>
    <path fill="var(--orange)" d="M395 0 L620 0 L620 360 L360 360 L478 258 Q505 232 488 200 Z"/>
  </svg>
  <div class="brand">
    <span class="brand-square"></span>
    <div>
      <div class="brand-main">CORAL RIDGE</div>
      <div class="brand-sub">DESIGN STUDIO LTD</div>
    </div>
  </div>
</section>

<section class="card card-back" aria-label="Card back">
  <svg class="card-shapes" viewBox="0 0 620 360" aria-hidden="true">
    <path fill="var(--orange)" d="M235 0 L545 0 L620 55 L620 255 L558 360 L235 360 L132 228 Q112 200 132 172 Z"/>
  </svg>
  <div class="brand">
    <span class="brand-square"></span>
    <div>
      <div class="brand-main">CORAL RIDGE</div>
      <div class="brand-sub">DESIGN STUDIO LTD</div>
    </div>
  </div>

  <div class="holder">
    <div class="holder-name">Marlon Whitfield</div>
    <div class="holder-title">Managing Director</div>
  </div>

  <address class="address">
    Seabreeze Plaza, Unit #5<br>
    P.O. Box 30476<br>
    Westhaven WH2-2040<br>
    Palm Coast Isles
  </address>

  <ul class="contacts">
    <li>
      <svg viewBox="0 0 16 16" aria-label="Phone"><path fill="#fff" d="M3 1 L6 1 L7 5 L5 6.5 Q6.5 9.5 9.5 11 L11 9 L15 10 L15 13 Q15 15 13 15 Q1 14 1 3 Q1 1 3 1 Z"/></svg>
      <span>: (555) 610-4827</span>
    </li>
    <li>
      <svg viewBox="0 0 16 16" aria-label="Fax"><rect x="4" y="1" width="8" height="4" fill="#fff"/><rect x="1" y="5" width="14" height="7" rx="1" fill="#fff"/><rect x="4" y="10" width="8" height="5" fill="#fff" stroke="var(--orange)" stroke-width="1"/></svg>
      <span>: (555) 610-4828</span>
    </li>
    <li>
      <svg viewBox="0 0 16 16" aria-label="Email"><rect x="1" y="3" width="14" height="10" fill="#fff"/><path d="M1 3 L8 9 L15 3" fill="none" stroke="var(--orange)" stroke-width="1.2"/></svg>
      <span>: marlon@crds.site</span>
    </li>
    <li>
      <svg viewBox="0 0 16 16" aria-label="Website"><circle cx="8" cy="8" r="6.5" fill="none" stroke="#fff" stroke-width="1.2"/><ellipse cx="8" cy="8" rx="3" ry="6.5" fill="none" stroke="#fff" stroke-width="1"/><path d="M1.5 8 H14.5 M2.5 5 H13.5 M2.5 11 H13.5" stroke="#fff" stroke-width="1"/></svg>
      <span>: www.crds.site</span>
    </li>
  </ul>
</section>

</body>
</html>
```